Silver Ridge Harlow Basin Masters Week of Golf 2107

I would like a design for an A4 Event Flyer.

This is a golf event for Senior ladies and gentlemen. I would like the design to appeal to an older age group.

I would like somewhere on the flyer a golf ball image with the following details inside "Please put me on your notice board"

The information on the Flyer is as follows
- (Title - Silver ridge Harlow Basin Masters Week of Golf 2017)
- Date 16th of October to 20th of October
- Over 55 years of age
- We invite our fellow Veteran Ladies and Gentlemen to play a unique 54 hole stableford event at three fantastic Golf Courses, and finish the week at Penwick Golf club with a 2BBB Medley.
- Insert schedule that is attached in PDF. They layout can be changed.

- For entry form and details
Contact: Penwick Proshop on 02 69318842 or email admin@penwickdalbrookgolf.example.au

I have attached 4 golf course images. This is a photo of each course. Could I please get these added to the flyer.

Target Market(s)

seniors

Industry/Entity Type

Golf Course

Requirements
Must have
• All information provided

```html
<!DOCTYPE html>
<html lang="en">
<head>
<meta charset="utf-8">
<title>Silver Ridge Harlow Basin Masters Week of Golf 2017</title>
<link href="https://fonts.googleapis.com/css2?family=Poppins:ital,wght@0,600;0,700;1,700;1,800;1,900&family=Roboto+Condensed:wght@700&display=swap" rel="stylesheet">
<style>
  :root {
    --green: #7cc242;
    --green-light: #a6d86e;
    --green-deep: #3f7a2c;
    --sky: #3f79c4;
    --charcoal: #333333;
    --band-dark: rgba(40, 40, 40, 0.88);
    --white: #ffffff;
  }
  * { margin: 0; padding: 0; box-sizing: border-box; }
  html, body { width: 848px; height: 1200px; overflow: hidden; background: var(--white); }
  .flyer {
    position: relative; width: 848px; height: 1200px; overflow: hidden;
    font-family: "Poppins", sans-serif; color: var(--white);
  }
  .hero-photo {
    position: absolute; left: 0; top: 0; width: 848px; height: 560px;
    background:
      radial-gradient(ellipse 190px 240px at 150px 250px, rgba(52,78,40,0.92) 0%, rgba(70,96,52,0.7) 55%, rgba(70,96,52,0) 100%),
      radial-gradient(ellipse 130px 160px at 540px 60px, rgba(58,84,44,0.85) 0%, rgba(58,84,44,0) 100%),
      radial-gradient(ellipse 250px 330px at 640px 330px, rgba(232,238,246,0.98) 0%, rgba(196,214,236,0.9) 50%, rgba(196,214,236,0) 100%),
      radial-gradient(ellipse 120px 140px at 480px 170px, rgba(226,178,150,0.95) 0%, rgba(226,178,150,0) 100%),
      radial-gradient(ellipse 110px 130px at 700px 170px, rgba(232,190,165,0.9) 0%, rgba(232,190,165,0) 100%),
      linear-gradient(180deg, #2a5fb0 0%, #4f86cc 45%, #a9c6e6 100%);
  }
  .title-band {
    position: absolute; left: 0; top: 388px; width: 848px; height: 170px;
    background: linear-gradient(90deg, rgba(124,194,66,0.96) 0%, rgba(124,194,66,0.88) 55%, rgba(166,216,110,0.4) 100%);
  }
  .title { position: absolute; left: 34px; top: 392px; font-style: italic; font-weight: 800; line-height: 1; }
  .title .line-1 { font-size: 68px; display: block; letter-spacing: 0.5px; }
  .title .line-2 { font-size: 30px; display: block; margin-top: 2px; }
  .title .line-3 { font-size: 48px; display: block; margin-top: 2px; }
  .intro-band {
    position: absolute; left: 0; top: 558px; width: 848px; height: 84px;
    background: var(--band-dark);
  }
  .intro {
    position: absolute; left: 50px; top: 569px; width: 750px; text-align: center;
    font-style: italic; font-weight: 800; font-size: 16.5px; line-height: 1.32;
  }
  .course-photo {
    position: absolute; left: 0; top: 642px; width: 848px; height: 106px;
    background: linear-gradient(180deg, #4d6a3a 0%, #7fae48 40%, #6fa63a 100%);
  }
  .lower-photo {
    position: absolute; left: 0; top: 748px; width: 848px; height: 320px;
    background: linear-gradient(180deg, #eef0ec 0%, #e3e8de 60%, #cbd7bd 100%);
  }
  .golf-ball {
    position: absolute; left: 58px; top: 700px; width: 374px; height: 374px; border-radius: 50%;
    background: radial-gradient(circle at 58% 35%, #ffffff 0%, #f0f0f0 40%, #c9c9c9 80%, #9c9c9c 100%);
  }
  .program-heading {
    position: absolute; left: 165px; top: 738px; color: #111; font-style: italic; font-weight: 800; font-size: 27px;
  }
  .program { position: absolute; left: 60px; top: 786px; width: 382px; color: #111; font-family: "Roboto Condensed", sans-serif; font-weight: 700; font-size: 12px; }
  .program-row { position: relative; height: 38.5px; }
  .program-row .day { position: absolute; right: 292px; top: 0; text-align: right; white-space: nowrap; }
  .program-row .day.small { font-size: 10.5px; }
  .program-row .date { position: absolute; left: 120px; top: 0; }
  .program-row .date.small { font-size: 10.5px; }
  .program-row .venue { position: absolute; right: 0; top: 0; text-align: right; white-space: nowrap; }
  .program-row .event {
    position: absolute; right: 0; top: 15px; background: var(--green); padding: 1px 4px; white-space: nowrap;
  }
  .program-row .leisure { position: absolute; left: 276px; top: 0; }
  .notice {
    position: absolute; left: 120px; top: 1030px; width: 250px; text-align: center;
    color: var(--charcoal); font-style: italic; font-weight: 700; font-size: 12px;
  }
  .dates { position: absolute; left: 496px; top: 782px; color: var(--charcoal); font-style: italic; font-weight: 800; line-height: 0.95; }
  .dates .range { display: block; font-size: 58px; }
  .dates .range sup { font-size: 29px; vertical-align: 24px; }
  .dates .month { display: block; font-size: 78px; margin-left: -4px; }
  .age-tag {
    position: absolute; left: 478px; top: 914px; width: 370px; height: 42px; background: var(--green);
    clip-path: polygon(14px 0, 100% 0, 100% 100%, 0 100%);
    font-style: italic; font-weight: 800; font-size: 24px; padding-left: 26px; line-height: 42px;
  }
  .footer-photo {
    position: absolute; left: 0; top: 1066px; width: 848px; height: 134px;
    background: linear-gradient(180deg, #4e8a33 0%, #3f7a2c 60%, #2f6322 100%);
  }
  .footer { position: absolute; left: 0; top: 1066px; width: 848px; text-align: center; font-style: italic; font-weight: 800; }
  .footer .dinner { font-size: 19.5px; margin-top: 1px; letter-spacing: 0.3px; }
  .footer .rule { width: 572px; height: 2px; background: var(--white); margin: 0 auto; position: relative; left: 30px; }
  .footer .time { font-size: 40px; line-height: 1.02; margin-top: 1px; }
  .footer .entry { font-size: 18.5px; line-height: 1.15; }
  .footer .contact { font-size: 13.3px; line-height: 1.4; }
</style>
</head>
<body>
<div class="flyer">
  <div class="hero-photo" role="img" aria-label="Photo of a smiling senior couple holding golf clubs under palm trees and blue sky"></div>
  <div class="title-band"></div>
  <h1 class="title">
    <span class="line-1">Silver Ridge</span>
    <span class="line-2">Harlow Basin Masters</span>
    <span class="line-3">Week of Golf 2017</span>
  </h1>

  <div class="intro-band"></div>
  <p class="intro">We invite our fellow Veteran Ladies and Gentlemen to play a unique 54 hole stableford event at three fantastic Golf Courses, and finish the week at Penwick Golf club with a 2BBB Medley.</p>

  <div class="course-photo" role="img" aria-label="Photo of a golf course fairway with a green, flag and bunker"></div>
  <div class="lower-photo" role="img" aria-label="Faded photo of a tree-lined golf course"></div>

  <div class="golf-ball" role="img" aria-label="Photo of a white golf ball"></div>
  <h2 class="program-heading">PROGRAM</h2>
  <div class="program">
    <div class="program-row"><span class="day">Sunday</span><span class="date">15 October</span><span class="venue">Penwick Golf Club</span><span class="event">Registrations : 4:00 PM-6:00 PM</span></div>
    <div class="program-row"><span class="day">Monday</span><span class="date">16 October</span><span class="venue">Kestrel Bay Golf Course Par 72</span><span class="event">Stableford - 1st Round Championships</span></div>
    <div class="program-row"><span class="day small">HBVGA Trophy Day</span><span class="date small">17 October</span><span class="venue" style="font-size:10.5px">Marlow Golf Course Par Par 71</span><span class="event">Stableford - 2nd Round Championships</span></div>
    <div class="program-row"><span class="day">Wednesday</span><span class="date">18 October</span><span class="leisure">LEISURE</span></div>
    <div class="program-row"><span class="day">Thursday</span><span class="date">19 October</span><span class="venue">Ashgrove Golf Course Par 72</span><span class="event">Stableford - Round 3 Championships</span></div>
    <div class="program-row"><span class="day">Friday</span><span class="date">20 October</span><span class="venue" style="right:14px">Penwick Golf Course Par 66</span><span class="event" style="right:32px">18 Hole 2BBB Medley Stableford</span></div>
  </div>
  <p class="notice">Please put me on your notice board</p>

  <div class="dates">
    <span class="range">16<sup>th</sup> to 20<sup>th</sup></span>
    <span class="month">October</span>
  </div>
  <div class="age-tag">Over 55 Years of Age</div>

  <div class="footer-photo" role="img" aria-label="Photo of a green golf course fairway from above"></div>
  <footer class="footer">
    <p class="dinner">PENWICK GOLF CLUB~ PRESENTATION DINNER DANCE</p>
    <div class="rule"></div>
    <p class="time">7:00 PM FOR 7:30</p>
    <p class="entry">For Entry Form and Details</p>
    <p class="contact">Penwick Proshop on &nbsp;|&nbsp; 02 69318842 or email &nbsp;|&nbsp; admin@penwickdalbrookgolf.example.au</p>
  </footer>
</div>
</body>
</html>
```